Shopify Design for wedding invitations

We are a greeting card manufactory, special in wedding invitation
I need a shopify website for our wedding invitation brand. (Lovonna), atttach you can find our logo.
We are looking for someone to create a modern and clean looking e-commerce store for our wedding invitation through Shopify. We need some life, professionalism and style put into our site. We will have a variety serie of products : laser cut wedding invitation, popup wedding invitaiton, vintage wedding invitation, handmade wedding invitation, printing invitation, Custom wedding cards, wedding stationery (including favor box, table card, place card, escort card, number card), Thank you card. our online store requires easy navigation to categories divided by product type.

our market is , Eourpe and USA,
please choose a good color for it.
you can go to our website: www.bluepinecrafts.com and check our product.
also you can go to Shopvane 4 new items.
https://www.shopvane.com/dp/K47T8M2Q61?ref=myi_title_dp

Designs look the same

Target Market(s)

Europe and USA

Industry/Entity Type

wedding

Number of Pages Required

1 page

Requirements
Must have
• Logo, 3 banners than can be changed each 3-5 seconds.
Nice to have
• nice icon and font, beautiful color,

```html
<!DOCTYPE html>
<html lang="en">
<head>
<meta charset="utf-8">
<title>Lovonna – Wedding Invitations</title>
<link href="https://fonts.googleapis.com/css2?family=Prata&family=Poppins:ital,wght@0,400;0,500;0,600;1,400&display=swap" rel="stylesheet">
<style>
:root{
  --green:#6ea335;
  --green-dark:#5b8d29;
  --brown:#4b2711;
  --cream:#fbf7f2;
  --footer:#fbf3ee;
  --text:#333;
  --muted:#777;
  --line:#e6ddd3;
}
*{box-sizing:border-box;margin:0;padding:0}
html,body{width:1200px;height:3562px;overflow:hidden}
body{position:relative;background:#fff;font-family:"Poppins",sans-serif;color:var(--text)}
.abs{position:absolute}
.serif{font-family:"Prata",serif}
a{color:inherit;text-decoration:none}

/* header */
.hero-bg{left:0;top:0;width:1200px;height:712px;background:var(--cream);overflow:hidden}
.deco-circle{border-radius:50%;background:#f1ebe4}
.brand{left:60px;top:40px;font-family:"Prata",serif;font-size:38px;color:var(--brown)}
.nav{left:472px;top:30px;display:flex;gap:18px;font-size:12px;color:#333}
.nav .active{color:var(--green);border-bottom:1px solid var(--green);padding-bottom:4px}
.search{left:888px;top:19px;width:251px;height:39px;border:1px solid #333;border-radius:20px;background:#fff;font-size:10.5px;color:#888;padding:12px 14px}
.search-btn{right:3px;top:3px;width:31px;height:31px;border-radius:50%;background:var(--green)}
.hero-title{left:66px;top:212px;font-family:"Prata",serif;font-size:66px;line-height:70px;color:var(--brown)}
.hero-sub{left:69px;top:440px;font-size:17px;line-height:25px;color:#222}
.btn{display:flex;align-items:center;background:var(--green);color:#fff;border-radius:22px;font-family:"Prata",serif;font-size:15px}
.btn .ico{width:34px;height:34px;border-radius:50%;background:#fff;margin:3px 14px 3px 3px;display:flex;align-items:center;justify-content:center}
.hero-btn{left:68px;top:503px;width:160px;height:40px}
.slider-line{left:60px;top:662px;width:75px;height:1px;background:var(--brown)}
.arrow-c{width:42px;height:42px;border-radius:50%;border:1.5px solid var(--brown);display:flex;align-items:center;justify-content:center}
.green-circle{left:802px;top:124px;width:526px;height:526px;border-radius:50%;background:#7aaa4a}
.hero-card{left:570px;top:187px;width:435px;height:435px;background:linear-gradient(135deg,#eccfae,#d9a878 55%,#e8c8a4)}
.float-bar{right:0;top:263px;display:flex;flex-direction:column;gap:8px}
.float-item{width:40px;height:34px;border-radius:17px 0 0 17px;background:#1c8ff0;margin-left:auto}
.float-item.g{background:#2bc34a}.float-item.o{background:#f5a316}
.float-chat{width:90px;height:34px;border-radius:17px 0 0 17px;background:#19a9e8;color:#fff;font-size:14px;display:flex;align-items:center;padding-left:12px;gap:8px}
.float-chat i{width:20px;height:20px;border-radius:50%;border:2px solid #fff;display:block}

/* section headings */
.h-sec{left:0;width:1200px;text-align:center;font-family:"Prata",serif;font-size:32px;color:var(--brown)}

/* categories */
.cat{top:860px;width:162px;height:187px;border-radius:6px;color:#fff;font-family:"Prata",serif;font-size:14px;line-height:19px;text-align:center;display:flex;flex-direction:column;justify-content:flex-end;padding-bottom:16px}
.cat .pic{position:absolute;left:30px;top:18px;width:102px;height:92px;border-radius:6px;background:rgba(255,255,255,.25)}
.cat.c2{outline:1px solid #a9b48d;outline-offset:3px}

/* products */
.sub{left:0;width:1200px;text-align:center;font-size:12px;font-style:italic;line-height:20px;color:#666}
.prod{top:1272px;width:228px;height:290px;border:1px solid #d9c8b8;padding:3px}
.prod .pic{width:100%;height:100%}
.price{top:1588px;width:228px;text-align:center;color:var(--green);font-size:14px;font-weight:500}
.pname{top:1616px;width:228px;text-align:center;font-family:"Prata",serif;font-size:14px;line-height:20px;color:#222}
.cart-btn{left:27px;top:140px;width:172px;height:40px;border:1.5px solid #fff;background:rgba(110,163,53,.55)}
.circle-arrow{width:52px;height:52px;border-radius:50%;border:1px solid #333;display:flex;align-items:center;justify-content:center;background:#fff}

/* about */
.about-left{left:75px;top:1770px;width:525px;height:463px;background:#f3ede6}
.about-right{left:600px;top:1770px;width:525px;height:463px;background:var(--green);color:#fff;padding:72px 50px 0 62px}
.about-right h2{font-family:"Prata",serif;font-weight:400;font-size:31px}
.about-right h3{font-size:15px;font-style:italic;font-weight:400;margin:2px 0 26px}
.about-right p{font-size:11.5px;line-height:19.5px;margin-bottom:20px}

/* news */
.news{top:2385px;width:270px;height:314px;border:1px solid #e2dbd3;background:#fff}
.news .pic{height:104px;background:linear-gradient(180deg,#5a3a2a,#a0673d 55%,#e4b584)}
.news .date{position:absolute;left:26px;top:0;width:69px;height:83px;background:var(--green);color:#fff;font-family:"Prata",serif;font-size:16px;line-height:21px;text-align:center;padding-top:10px;border-radius:0 0 4px 4px}
.news h4{font-family:"Prata",serif;font-weight:400;font-size:15.5px;line-height:22px;color:#222;margin:38px 22px 12px}
.news p{font-size:11px;line-height:19.5px;color:#777;margin:0 22px}

/* promo */
.promo{top:2761px;height:181px;border:1.5px solid #e9d6c6;background:#fff}
.promo .pic{position:absolute;left:20px;top:32px;width:126px;height:110px;border-radius:8px}
.promo .pic.round{border-radius:50%;left:22px;top:30px;width:112px;height:112px}
.promo h4{position:absolute;font-family:"Prata",serif;font-weight:400;font-size:22px;color:var(--brown)}
.promo p{position:absolute;font-size:11px;line-height:20px;color:#666;width:220px}
.promo .btn{position:absolute;width:160px;height:40px}

/* newsletter */
.footer-bg{left:0;top:3149px;width:1200px;height:413px;background:var(--footer)}
.news-band{left:60px;top:3051px;width:1079px;height:170px;border-radius:85px;background:var(--brown)}
.person-bg{left:131px;top:3108px;width:188px;height:113px;border-radius:94px 94px 0 0;background:var(--green)}
.person{left:150px;top:3018px;width:150px;height:203px;background:linear-gradient(180deg,#a25a2e,#e9d3c3 45%,#b2402f)}
.nl-title{left:340px;top:3088px;font-family:"Prata",serif;font-size:29px;color:#fff}
.nl-sub{left:342px;top:3133px;font-size:12px;line-height:19px;font-style:italic;color:#f4e6dc}
.nl-input{left:704px;top:3093px;width:370px;height:39px;border-radius:20px;background:#fff;font-size:11px;color:#555;padding:12px 18px}
.nl-btn{left:704px;top:3138px;width:370px;height:40px;border-radius:20px;background:var(--green);color:#fff;font-family:"Prata",serif;font-size:15px;text-align:center;line-height:40px}
.nl-btn i{position:absolute;left:3px;top:3px;width:34px;height:34px;border-radius:50%;background:#fff}

/* footer */
.f-brand{left:60px;top:3320px;font-family:"Prata",serif;font-size:50px;color:var(--brown)}
.social{top:3407px;width:40px;height:40px;border-radius:50%;border:1.5px solid var(--green);display:flex;align-items:center;justify-content:center}
.social i{width:12px;height:12px;border-radius:50%;background:var(--green);display:block}
.f-head{top:3267px;font-family:"Prata",serif;font-size:17px;color:var(--brown)}
.f-list{list-style:none;font-size:11.5px;color:#333;line-height:21px}
.f-list.dots li::before{content:"";display:inline-block;width:4px;height:4px;border-radius:50%;background:var(--green);margin:0 12px 2px 0;vertical-align:middle}
.f-row{display:flex;gap:14px;align-items:flex-start;font-size:11.5px;line-height:21px;color:#333;margin-bottom:8px}
.f-row svg{flex:none;margin-top:3px}
.f-line{left:60px;top:3516px;width:1079px;height:1px;background:#e1d4ca}
.copy{left:0;top:3532px;width:1200px;text-align:center;font-size:11px;color:#333}
.copy b{font-weight:400;color:var(--green)}
</style>
</head>
<body>

<!-- header / hero -->
<div class="abs hero-bg">
  <div class="abs deco-circle" style="left:0;top:138px;width:166px;height:166px"></div>
  <div class="abs deco-circle" style="left:-30px;top:608px;width:110px;height:110px"></div>
  <div class="abs green-circle"></div>
  <div class="abs hero-card" role="img" aria-label="Laser cut gold wedding invitation card with floral wreath"></div>
</div>

<div class="abs brand">Lovonna</div>
<nav class="abs nav">
  <a class="active">Home</a><a>Products</a><a>News</a><a>About Us</a><a>Contact Us</a><a>Send Inquiry</a>
</nav>
<div class="abs search">Please Enter Keyword
  <div class="abs search-btn"><svg width="31" height="31" viewBox="0 0 31 31"><circle cx="14" cy="14" r="6" fill="none" stroke="#fff" stroke-width="2"/><line x1="18.5" y1="18.5" x2="22" y2="22" stroke="#fff" stroke-width="2"/></svg></div>
</div>

<h1 class="abs hero-title" style="font-weight:400">Happy<br>Wedding<br>Season</h1>
<p class="abs hero-sub">Pass you's Happiness And Joy In the<br>Important Days Of Your Life</p>
<a class="abs btn hero-btn"><span class="ico"><svg width="18" height="16" viewBox="0 0 18 16"><path d="M1 5h16l-2 10H3z" fill="none" stroke="#6ea335" stroke-width="1.5"/><path d="M6 5l3-4 3 4" fill="none" stroke="#6ea335" stroke-width="1.5"/></svg></span>SHOP NOW</a>

<div class="abs slider-line"></div>
<div class="abs arrow-c" style="left:135px;top:641px"><svg width="10" height="14"><path d="M8 1L2 7l6 6" fill="none" stroke="#4b2711" stroke-width="1.5"/></svg></div>
<div class="abs arrow-c" style="left:183px;top:641px;border-color:var(--green)"><svg width="10" height="14"><path d="M2 1l6 6-6 6" fill="none" stroke="#6ea335" stroke-width="1.5"/></svg></div>

<div class="abs float-bar">
  <div class="float-item"></div>
  <div class="float-item g"></div>
  <div class="float-chat"><i></i>Chat</div>
  <div class="float-item g"></div>
  <div class="float-item o"></div>
  <div class="float-item"></div>
</div>

<!-- categories -->
<h2 class="abs h-sec" style="top:784px;font-weight:400">Categories</h2>
<svg class="abs" style="left:32px;top:938px" width="14" height="32"><path d="M12 1L2 16l10 15" fill="none" stroke="#555" stroke-width="1.2"/></svg>
<svg class="abs" style="left:1154px;top:938px" width="14" height="32"><path d="M2 1l10 15-10 15" fill="none" stroke="#555" stroke-width="1.2"/></svg>

<div class="abs cat" style="left:65px;background:#a8485a"><div class="pic" role="img" aria-label="Wedding invitation card"></div>Wedding Invitation<br>Card</div>
<div class="abs cat c2" style="left:246px;background:#a9b48d"><div class="pic" role="img" aria-label="Laser cut favor boxes"></div>Laser Cut Favor<br>Box</div>
<div class="abs cat" style="left:433px;background:#c9a7f0"><div class="pic" role="img" aria-label="Wedding stationery place cards"></div>Wedding<br>Stationery</div>
<div class="abs cat" style="left:612px;background:#6fbcb0"><div class="pic" role="img" aria-label="Wedding decoration accessories"></div>Wedding Decoration<br>Assessories</div>
<div class="abs cat" style="left:795px;background:#d9828a"><div class="pic" role="img" aria-label="3D pop up card"></div>3d PoP Up<br>Card</div>
<div class="abs cat" style="left:973px;background:#6a6bb8"><div class="pic" role="img" aria-label="Greeting card"></div>Greeting<br>Card</div>

<!-- new products -->
<h2 class="abs h-sec" style="top:1132px;font-weight:400">New Products</h2>
<p class="abs sub" style="top:1182px">Lorem ipsum has been the industry's standard dummy text ever since the 1500s,<br>when an unknown printer took a galley of type scrambled</p>

<div class="abs circle-arrow" style="left:59px;top:1398px"><svg width="26" height="14"><path d="M25 7H2M8 1L2 7l6 6" fill="none" stroke="#333" stroke-width="1.2"/></svg></div>
<div class="abs circle-arrow" style="left:1089px;top:1398px"><svg width="26" height="14"><path d="M1 7h23M18 1l6 6-6 6" fill="none" stroke="#333" stroke-width="1.2"/></svg></div>

<div class="abs prod" style="left:124px"><div class="pic" role="img" aria-label="Green laser cut pocket invitation" style="background:linear-gradient(160deg,#7aa84a,#5f8f33)"></div>
  <a class="abs btn cart-btn"><span class="ico"><svg width="18" height="16" viewBox="0 0 18 16"><path d="M1 5h16l-2 10H3z" fill="none" stroke="#6ea335" stroke-width="1.5"/><path d="M6 5l3-4 3 4" fill="none" stroke="#6ea335" stroke-width="1.5"/></svg></span>ADD TO CART</a></div>
<div class="abs prod" style="left:369px"><div class="pic" role="img" aria-label="Teal laser cut invitation card" style="background:linear-gradient(160deg,#f3f1ee,#6cc2ad 50%,#e8e5df)"></div></div>
<div class="abs prod" style="left:608px"><div class="pic" role="img" aria-label="Kraft envelope with gold laser cut invitation" style="background:linear-gradient(160deg,#5a3621,#c89a66 55%,#6b412a)"></div></div>
<div class="abs prod" style="left:848px"><div class="pic" role="img" aria-label="Pearl white embossed floral card" style="background:linear-gradient(160deg,#f2efe8,#d7d1c5 60%,#eee9df)"></div></div>

<div class="abs price" style="left:124px">US $0.81 - US $1.17</div>
<div class="abs price" style="left:369px">US $0.81 - US $1.17</div>
<div class="abs price" style="left:608px">US $0.81 - US $1.17</div>
<div class="abs price" style="left:848px">US $0.81 - US $1.17</div>
<div class="abs pname" style="left:124px">Custome Pocket Card Red<br>invitations For...</div>
<div class="abs pname" style="left:369px">Custome Pocket Card Red<br>invitations For...</div>
<div class="abs pname" style="left:608px">Custome Pocket Card Red<br>invitations For...</div>
<div class="abs pname" style="left:848px">Custome Pocket Card Red<br>invitations For...</div>

<!-- about -->
<div class="abs about-left"><div class="abs" role="img" aria-label="Laser cut invitation with kraft envelope and floral insert" style="left:120px;top:90px;width:300px;height:290px;border-radius:6px;background:linear-gradient(135deg,#c9925d,#efe6da 50%,#c9a3a8)"></div></div>
<div class="abs about-right">
  <h2>About Us</h2>
  <h3>Hangzhou Blue Pine Stationery Co., Ltd.</h3>
  <p>Our Company is established in 2001, located in Hang Zhou, Zhejiang Province. We are an professional Manufacturer and Exporter that is concerned with the design, Development and Production manufacturing Wedding invitation Card, favor boxes and other gift items.</p>
  <p>Our Company Products all passed the QSA, EPC and TSR accreditation. We are able to provide high- quality products to customers from around the world, main market Areas include Europe (Germany, UK, France, Italy) USA, Asian (Japan, Korea, India), South America. We have always been the most trusted partner of our customers.</p>
</div>

<!-- news -->
<h2 class="abs h-sec" style="top:2306px;font-weight:400">Latest News</h2>
<div class="abs news" style="left:174px"><div class="pic" role="img" aria-label="Trade fair booth"></div><div class="date">15<br>Dec<br>2020</div>
  <h4>2020 The 18th Eastbay International Gifts, Premiums</h4>
  <p>Hangzhou Blue Pine Stationery Company attended The 18th Eastbay International Gifts, Premiums and Housewares Exhivition , December.2020</p></div>
<div class="abs news" style="left:465px"><div class="pic" role="img" aria-label="Gift fair hall" style="background:linear-gradient(180deg,#3b3b3b,#b99a78 55%,#ead8c0)"></div><div class="date">27<br>April<br>2020</div>
  <h4>2019 Harbourline Gifts &amp; Premium Fair</h4>
  <p>Hangzhou Blue Pine Stationery Company attended Harbourline Gifts &amp; Premium Fair, April 2019</p></div>
<div class="abs news" style="left:758px"><div class="pic" role="img" aria-label="Trade fair booth"></div><div class="date">15<br>Dec<br>2020</div>
  <h4>2020 The 18th Eastbay International Gifts, Premiums</h4>
  <p>Hangzhou Blue Pine Stationery Company attended The 18th Eastbay International Gifts, Premiums and Housewares Exhivition , December.2020</p></div>

<!-- promo -->
<div class="abs promo" style="left:174px;width:419px">
  <div class="pic" role="img" aria-label="Thank you card with flower box" style="background:linear-gradient(160deg,#d6a05a,#5460b0 60%,#7b86cf)"></div>
  <h4 style="left:187px;top:28px">Thank You card</h4>
  <p style="left:189px;top:60px">Lorem Ipsum has been the industry's standard dummy text ever..</p>
  <a class="btn" style="left:184px;top:108px"><span class="ico"><svg width="18" height="16" viewBox="0 0 18 16"><path d="M1 5h16l-2 10H3z" fill="none" stroke="#6ea335" stroke-width="1.5"/><path d="M6 5l3-4 3 4" fill="none" stroke="#6ea335" stroke-width="1.5"/></svg></span>SHOP NOW</a>
</div>
<div class="abs promo" style="left:610px;width:417px">
  <div class="pic round" role="img" aria-label="Wedding invitation set" style="background:radial-gradient(circle,#f2e9d8,#e0c9a5)"></div>
  <h4 style="left:158px;top:28px">Online Store</h4>
  <p style="left:160px;top:60px">Lorem Ipsum has been the industry's standard dummy text ever..</p>
  <a class="btn" style="left:155px;top:108px"><span class="ico"><svg width="18" height="16" viewBox="0 0 18 16"><path d="M1 5h16l-2 10H3z" fill="none" stroke="#6ea335" stroke-width="1.5"/><path d="M6 5l3-4 3 4" fill="none" stroke="#6ea335" stroke-width="1.5"/></svg></span>SHOP NOW</a>
</div>

<!-- newsletter -->
<div class="abs footer-bg"></div>
<div class="abs news-band"></div>
<div class="abs person-bg"></div>
<div class="abs person" role="img" aria-label="Bride in hat and lace top"></div>
<h3 class="abs nl-title" style="font-weight:400">Newsletter Signup !</h3>
<p class="abs nl-sub">Would you like to receive our exclusive update for<br>signup our Newsletter !</p>
<div class="abs nl-input">Enter Email *</div>
<div class="abs nl-btn"><i></i>SUBSCRIBE</div>

<!-- footer -->
<div class="abs f-brand">Lovonna</div>
<div class="abs social" style="left:106px"><i></i></div>
<div class="abs social" style="left:152px"><i></i></div>
<div class="abs social" style="left:197px"><i></i></div>

<h4 class="abs f-head" style="left:321px;font-weight:400">Sitemap</h4>
<ul class="abs f-list dots" style="left:321px;top:3308px">
  <li>Home</li><li>Products</li><li>studio</li><li>News</li><li>About Us</li><li>Contact Us</li><li>Send inquiry</li><li>Sitemap</li>
</ul>

<h4 class="abs f-head" style="left:502px;font-weight:400">Contact Us</h4>
<div class="abs" style="left:502px;top:3308px;width:200px">
  <div class="f-row"><svg width="16" height="20" viewBox="0 0 16 20"><path d="M8 19s6-7 6-11A6 6 0 0 0 2 8c0 4 6 11 6 11z" fill="none" stroke="#6ea335" stroke-width="1.3"/><circle cx="8" cy="8" r="2" fill="none" stroke="#6ea335" stroke-width="1.3"/></svg><span>Room 8, 4th Floor, Lanting building, Meiyu Road, Hangzhou, P.R CHINA, 310012</span></div>
  <div class="f-row" style="margin-top:6px"><svg width="16" height="16" viewBox="0 0 16 16"><path d="M3 1l3 3-2 2c1 3 3 5 6 6l2-2 3 3-2 2C7 15 1 9 1 3z" fill="none" stroke="#6ea335" stroke-width="1.2"/></svg><span>+86 13700421856</span></div>
  <div class="f-row"><svg width="16" height="16" viewBox="0 0 16 16"><path d="M3 1l3 3-2 2c1 3 3 5 6 6l2-2 3 3-2 2C7 15 1 9 1 3z" fill="none" stroke="#6ea335" stroke-width="1.2"/></svg><span>+86 05718842190</span></div>
</div>

<h4 class="abs f-head" style="left:740px;font-weight:400">Call Us On</h4>
<div class="abs" style="left:740px;top:3308px">
  <div class="f-row"><svg width="16" height="16" viewBox="0 0 16 16"><path d="M3 1l3 3-2 2c1 3 3 5 6 6l2-2 3 3-2 2C7 15 1 9 1 3z" fill="none" stroke="#6ea335" stroke-width="1.2"/></svg><span>+86 13700421856</span></div>
  <div class="f-row"><svg width="16" height="16" viewBox="0 0 16 16"><path d="M3 1l3 3-2 2c1 3 3 5 6 6l2-2 3 3-2 2C7 15 1 9 1 3z" fill="none" stroke="#6ea335" stroke-width="1.2"/></svg><span>+86 18860214573</span></div>
  <div class="f-row"><svg width="16" height="16" viewBox="0 0 16 16"><path d="M3 1l3 3-2 2c1 3 3 5 6 6l2-2 3 3-2 2C7 15 1 9 1 3z" fill="none" stroke="#6ea335" stroke-width="1.2"/></svg><span>+86 18860377104</span></div>
  <div class="f-row"><svg width="16" height="16" viewBox="0 0 16 16"><path d="M3 1l3 3-2 2c1 3 3 5 6 6l2-2 3 3-2 2C7 15 1 9 1 3z" fill="none" stroke="#6ea335" stroke-width="1.2"/></svg><span>+86 18860539218</span></div>
</div>

<h4 class="abs f-head" style="left:955px;font-weight:400">Email Us</h4>
<div class="abs" style="left:955px;top:3308px">
  <div class="f-row"><svg width="18" height="14" viewBox="0 0 18 14"><rect x="1" y="1" width="16" height="12" fill="none" stroke="#6ea335" stroke-width="1.2"/><path d="M1 1l8 7 8-7" fill="none" stroke="#6ea335" stroke-width="1.2"/></svg><span>admin@bluepinecrafts.com</span></div>
  <div class="f-row"><svg width="18" height="14" viewBox="0 0 18 14"><rect x="1" y="1" width="16" height="12" fill="none" stroke="#6ea335" stroke-width="1.2"/><path d="M1 1l8 7 8-7" fill="none" stroke="#6ea335" stroke-width="1.2"/></svg><span>Mira@bluepinecrafts.com</span></div>
  <div class="f-row"><svg width="18" height="14" viewBox="0 0 18 14"><rect x="1" y="1" width="16" height="12" fill="none" stroke="#6ea335" stroke-width="1.2"/><path d="M1 1l8 7 8-7" fill="none" stroke="#6ea335" stroke-width="1.2"/></svg><span>sales@bluepinecrafts.com</span></div>
  <div class="f-row"><svg width="18" height="14" viewBox="0 0 18 14"><rect x="1" y="1" width="16" height="12" fill="none" stroke="#6ea335" stroke-width="1.2"/><path d="M1 1l8 7 8-7" fill="none" stroke="#6ea335" stroke-width="1.2"/></svg><span>orders@bluepinecrafts.com</span></div>
  <div class="f-row"><svg width="18" height="14" viewBox="0 0 18 14"><rect x="1" y="1" width="16" height="12" fill="none" stroke="#6ea335" stroke-width="1.2"/><path d="M1 1l8 7 8-7" fill="none" stroke="#6ea335" stroke-width="1.2"/></svg><span>info@bluepinecrafts.com</span></div>
</div>

<div class="abs f-line"></div>
<p class="abs copy">©<b>Lovonna</b> - 2022 All rights reserved.</p>

</body>
</html>
```